Cobalt Field Services website design

We want to create a Sports turf website for our business Cobalt Field Services - we do sports turf management on sports fields around the Mackay region soccer rugby league softball fields etc from full turf management plans and maintenance to just supply and apply of turf management products and just supply of products with program we also do grounds facility maintenance at council facility's and grounds that require a higher level of care - we will up load our logos and fonts etc to assist with the colour pallet for the website - we will have to have a landing page a shop page with tabs a gallery tab along with a grants initiative and our northreach finest green tab also - our font for the txt is called ethnocentric
Updates

how do we open time for people to submit we have no one submitted

Industry/Entity Type

Turf

Coding

Coded - Design and coding required

Number of Pages Required

5+ page

Font styles to use
Other font styles liked:
• ethnocentric

Requirements
Must have
• I have mentioned some waffle in the description that should assist
Should not have
• anything not related

```html
<!DOCTYPE html>
<html lang="en">
<head>
<meta charset="utf-8">
<title>Cobalt Field Services</title>
<link href="https://fonts.googleapis.com/css2?family=Orbitron:wght@600;700;800;900&family=Poppins:wght@400;500;600;700&display=swap" rel="stylesheet">
<style>
:root{
  --green:#1a8b3c;
  --green-dark:#0c3a1c;
  --green-deep:#072613;
  --ink:#1b1b1b;
  --muted:#8a8a8a;
  --line:#d9d9d9;
  --white:#ffffff;
}
*{box-sizing:border-box;margin:0;padding:0}
html,body{width:1200px;height:5115px;overflow:hidden}
body{font-family:"Poppins",sans-serif;color:var(--ink);background:var(--white);position:relative}
.display{font-family:"Orbitron",sans-serif;text-transform:uppercase;letter-spacing:2px;font-weight:800}
section,footer{position:absolute;left:0;width:1200px}
.abs{position:absolute}
.photo{position:absolute}

/* HERO */
.hero{top:0;height:670px;background:linear-gradient(180deg,#33452c 0%,#3f6a2c 35%,#2f6a22 70%,#1f4a17 100%)}
.nav-logo{left:150px;top:25px;color:var(--white);font-family:"Orbitron",sans-serif;font-weight:800;font-size:11px;letter-spacing:.5px;white-space:nowrap}
.nav-links{left:390px;top:25px;display:flex;gap:12px;color:var(--white);font-size:12.5px;white-space:nowrap}
.nav-contact{left:920px;top:16px;width:130px;height:36px;background:var(--white);color:var(--ink);font-size:13px;font-weight:600;display:flex;align-items:center;justify-content:center}
.hero-title{left:150px;top:262px;color:var(--white);font-size:64px;line-height:92px;letter-spacing:4px;font-weight:900}
.hero-text{left:150px;top:470px;width:570px;color:#e8eee6;font-size:11.5px;line-height:18px}
.btn{display:flex;align-items:center;justify-content:center;color:var(--white);font-weight:600;font-size:14px}
.hero-btn{left:150px;top:557px;width:166px;height:44px;background:var(--green)}
.happy{left:845px;top:97px;color:var(--white);font-size:11px}
.watch{left:845px;top:124px;width:205px;height:54px;border-radius:27px;background:rgba(255,255,255,.35);display:flex;align-items:center;gap:14px;padding-left:4px;color:var(--white);font-size:19px}
.watch-icon{width:48px;height:48px;border-radius:50%;background:#111;display:flex;align-items:center;justify-content:center}
.stat{left:845px;top:200px;color:var(--white);font-family:"Orbitron",sans-serif;font-size:48px;font-weight:900}
.stat-label{left:845px;top:263px;color:var(--white);font-size:20px}
.avatars{left:845px;top:318px;display:flex}
.avatars span{width:32px;height:32px;border-radius:50%;border:2px solid var(--white);margin-right:-8px;background:#8b7a6b}
.avatars span.plus{background:var(--white);color:#111;display:flex;align-items:center;justify-content:center;font-weight:700;font-size:20px}

/* ABOUT */
.about{top:670px;height:697px;background:var(--white)}
.about-photo{left:143px;top:95px;width:372px;height:510px;background:linear-gradient(180deg,#1f4c9a 0%,#4f86c8 40%,#4a7b3a 62%,#2f6b22 100%)}
.about-title{left:543px;top:100px;font-size:28px;line-height:55px;color:var(--ink)}
.small{font-size:10px;line-height:19px;color:var(--muted)}
.about-text{left:543px;top:285px;width:490px}
.about-rule{left:543px;top:355px;width:490px;height:1px;background:#bfbfbf}
.feature{top:390px;width:240px}
.feature h4{font-size:15px;font-weight:500;line-height:22px;margin:14px 0 12px}
.feature a{display:block;margin-top:14px;color:var(--green);font-size:13px;text-decoration:none}

/* SERVICES */
.services{top:1367px;height:630px;background:linear-gradient(180deg,#0c3a1c 0%,#13542a 50%,#1a6e32 100%)}
.band-title{left:0;width:1200px;text-align:center;color:var(--white);font-size:30px;line-height:56px}
.card{position:absolute;width:288px;background:var(--white);padding:6px}
.card-head{display:flex;align-items:center;gap:20px;height:96px;padding-left:14px}
.card-icon{width:52px;height:52px;border-radius:50%;background:var(--green-deep);display:flex;align-items:center;justify-content:center;flex:none}
.card-head h3{font-size:13px;line-height:17px;color:var(--ink);letter-spacing:1.5px}
.card-photo{height:168px}
.services-btn{left:494px;top:530px;width:212px;height:48px;background:var(--green)}

/* PRODUCTS */
.products{top:1997px;height:817px}
.dark-title{left:0;width:1200px;text-align:center;font-size:30px;line-height:56px;color:#222}
.product-photo{left:150px;top:253px;width:418px;height:388px;background:radial-gradient(circle at 50% 50%,#e8e8e8 0%,#c9c9c9 22%,#4b8a2a 40%,#2f6b1e 100%)}
.cart-btn{left:150px;top:660px;width:418px;height:60px;background:linear-gradient(90deg,#0c3a1c,#062512)}
.product-list{left:604px;top:253px;width:446px}
.product-row{height:102px;border-bottom:1px solid var(--line);display:flex;align-items:center;gap:36px;position:relative}
.product-row .num{font-family:"Poppins",sans-serif;font-size:40px;font-weight:700;color:#9aa39d;width:56px}
.product-row .name{font-family:"Orbitron",sans-serif;font-weight:700;font-size:13px;letter-spacing:2px;color:#9aa39d;text-transform:uppercase;flex:1}
.product-row.active .num{color:var(--green-dark)}
.product-row.active .name{color:var(--ink)}

/* GRANTS */
.grants{top:2814px;height:520px;background:linear-gradient(180deg,#0c3a1c 0%,#13542a 60%,#1a6e32 100%)}
.grant-card{top:228px;height:226px;padding:22px 22px}
.grant-card h3{font-size:16px;line-height:24px;color:var(--ink);margin-bottom:30px}
.grant-card ul{list-style:none}
.grant-card li{font-size:10px;line-height:29px;display:flex;align-items:center;gap:8px;color:#333;white-space:nowrap}
.grant-card li::before{content:"";width:7px;height:7px;border-radius:50%;background:#111;flex:none}

/* GALLERY */
.gallery{top:3334px;height:759px}
.gal{position:absolute;display:flex;align-items:flex-end;justify-content:center;color:var(--white);font-size:14px;font-weight:600;padding-bottom:22px;text-transform:uppercase}
.gal-left{left:226px;top:258px;width:200px;height:270px;background:linear-gradient(180deg,#8fa9c4 0%,#6d7f8c 45%,#2a2e33 100%)}
.gal-right{left:783px;top:258px;width:190px;height:270px;background:linear-gradient(180deg,#4f7f3a 0%,#8fb0a6 45%,#273029 100%)}
.gal-center{left:413px;top:198px;width:374px;height:390px;background:linear-gradient(180deg,#7891a6 0%,#3d6c3a 45%,#10190f 100%);box-shadow:0 4px 16px rgba(0,0,0,.35);font-size:16px}

/* CONTACT */
.contact{top:4093px;height:680px}
.contact-item{top:190px;width:170px;text-align:center}
.contact-icon{width:42px;height:42px;background:var(--green-dark);margin:0 auto 10px;display:flex;align-items:center;justify-content:center}
.contact-item p{font-size:9.5px;line-height:14px;color:#333}
.field{position:absolute;height:48px;border:1px solid var(--line);border-radius:6px;font-size:11px;color:var(--muted);padding:15px 18px}
.submit{left:214px;top:539px;width:772px;height:48px;background:var(--green);font-weight:500}

/* FOOTER */
.footer{top:4773px;height:342px;background:linear-gradient(180deg,#0a1f10 0%,#07150b 100%);color:var(--white)}
.foot-logo{left:150px;top:96px;font-family:"Orbitron",sans-serif;font-weight:800;font-size:28px;letter-spacing:2px;line-height:36px}
.foot-logo small{display:block;font-size:14px;letter-spacing:10px;color:var(--white)}
.foot-tag{left:150px;top:182px;font-size:12px;line-height:21px;width:360px}
.foot-about{left:772px;top:68px;width:300px;font-size:13px;line-height:22px}
.socials{left:772px;top:166px;display:flex;gap:14px}
.socials span{width:32px;height:32px;border-radius:50%;border:2px solid var(--white)}
.foot-nav{left:155px;top:232px;display:flex;gap:26px;font-size:13px}
.foot-rule{left:150px;top:287px;width:900px;height:1px;background:#4a5a4e}
.foot-legal{left:0;top:313px;width:1200px;display:flex;justify-content:center;gap:34px;font-size:10.5px;color:#cfd6d0}
</style>
</head>
<body>

<section class="hero">
  <div class="photo" style="inset:0;background:linear-gradient(180deg,rgba(40,55,40,.55) 0%,rgba(50,110,40,.3) 40%,rgba(20,60,15,.5) 100%)" role="img" aria-label="Floodlit sports field with freshly cut green turf at dusk"></div>
  <div class="abs nav-logo">COBALT FIELD SERVICES</div>
  <nav class="abs nav-links"><span>Home</span><span>About Us</span><span>Services</span><span>Products</span><span>Grants Initiative</span><span>Gallery</span></nav>
  <div class="abs nav-contact">Contact us</div>
  <h1 class="abs hero-title display">Turf<br>Excellence.</h1>
  <p class="abs hero-text">Efficient shipping solutions for businesses and individuals. Get your goods delivered safely, on time, and at the best rates. Efficient shipping solutions for businesses and individuals. Get your goods delivered safely, on time, and at the best rates.</p>
  <div class="abs btn hero-btn">Get Started</div>
  <div class="abs happy">100k Happy Customers</div>
  <div class="abs watch"><span class="watch-icon"><svg width="16" height="18" viewBox="0 0 16 18"><path d="M2 1l13 8-13 8z" fill="#fff"/></svg></span>Watch Now</div>
  <div class="abs stat">200+</div>
  <div class="abs stat-label">Customers</div>
  <div class="abs avatars"><span style="background:#7c8a7a"></span><span style="background:#a08b78"></span><span style="background:#6f7d8c"></span><span class="plus">+</span></div>
</section>

<section class="about">
  <div class="photo about-photo" role="img" aria-label="Sports field under a blue sky with floodlight towers and trees"></div>
  <h2 class="abs about-title display">Expert Turf<br>Management with<br>Local Care</h2>
  <p class="abs small about-text">Experience hassle-free car buying with our extensive range of vehicles, transparent pi team dedicated to your satisfaction Experience hassle-free car buying with our</p>
  <div class="abs about-rule"></div>
  <div class="abs feature" style="left:543px">
    <svg width="56" height="56" viewBox="0 0 56 56"><circle cx="28" cy="28" r="22" fill="none" stroke="#0c3a1c" stroke-width="4"/><path d="M18 22l10-5 10 5v12l-10 5-10-5z" fill="#0c3a1c"/></svg>
    <h4>Product supply &amp;<br>application</h4>
    <p class="small">Experience hassle-free car b extensive range of vehicles, transparent pi team dedicated to your satisfaction Experience</p>
    <a>Lean More &rarr;</a>
  </div>
  <div class="abs feature" style="left:800px">
    <svg width="62" height="56" viewBox="0 0 62 56"><path d="M4 52c4-14 16-20 28-20s22 8 26 20z" fill="#0c3a1c"/><path d="M30 34L50 6" stroke="#0c3a1c" stroke-width="4"/><rect x="46" y="2" width="10" height="6" fill="#0c3a1c"/></svg>
    <h4>Grounds &amp; facility<br>maintenance</h4>
    <p class="small">Experience hassle-free car b extensive range of vehicles, transparent pi team dedicated to your satisfaction Experience</p>
    <a>Lean More &rarr;</a>
  </div>
</section>

<section class="services">
  <h2 class="abs band-title display" style="top:52px">From Turf Plans to<br>Perfect Grounds</h2>
  <div class="card" style="left:150px;top:215px">
    <div class="card-head"><span class="card-icon"><svg width="24" height="24" viewBox="0 0 24 24"><path d="M3 20h18M6 20V10h4v10M14 6l6 4v10" stroke="#fff" stroke-width="2" fill="none"/></svg></span><h3 class="display">Sport Turf<br>Management</h3></div>
    <div class="photo card-photo" style="position:relative;background:linear-gradient(180deg,#9a9aa8 0%,#5a8a3a 45%,#3f7a22 100%)" role="img" aria-label="Stadium pitch with a sprinkler watering the turf"></div>
  </div>
  <div class="card" style="left:456px;top:215px">
    <div class="card-head"><span class="card-icon"><svg width="24" height="24" viewBox="0 0 24 24"><path d="M4 8l8-4 8 4v9l-8 4-8-4z" stroke="#fff" stroke-width="2" fill="none"/></svg></span><h3 class="display">Products<br>Supply</h3></div>
    <div class="photo card-photo" style="position:relative;background:linear-gradient(180deg,#8fb0d2 0%,#c8d6dc 35%,#5f9a3a 55%,#3c7a24 100%)" role="img" aria-label="Artificial turf field with white line marking"></div>
  </div>
  <div class="card" style="left:762px;top:215px">
    <div class="card-head"><span class="card-icon"><svg width="24" height="24" viewBox="0 0 24 24"><path d="M12 3v18M6 9h12M7 15h10" stroke="#fff" stroke-width="2"/></svg></span><h3 class="display">Grounds<br>Facility<br>Maintenance</h3></div>
    <div class="photo card-photo" style="position:relative;background:linear-gradient(180deg,#6f9a3c 0%,#5e8f2e 50%,#4a8320 100%)" role="img" aria-label="Groundskeeper riding a mower across a park lawn"></div>
  </div>
  <div class="abs btn services-btn">View All Services</div>
</section>

<section class="products">
  <h2 class="abs dark-title display" style="top:95px">High-Quality Products for<br>Healthy Turf</h2>
  <div class="photo product-photo" role="img" aria-label="Gloved hands holding a bag of white fertilizer granules over grass"></div>
  <div class="abs btn cart-btn">Add to card</div>
  <div class="abs product-list">
    <div class="product-row active" style="height:78px;align-items:flex-start;padding-top:4px"><span class="num">01</span><span class="name" style="padding-top:18px">Turf Fertilizers</span><svg width="40" height="46" viewBox="0 0 40 46"><path d="M20 2l6 8h-12zM12 14h16v28H12z" fill="#0c3a1c"/></svg></div>
    <div class="product-row"><span class="num">02</span><span class="name">Grass Seeds</span><svg width="46" height="40" viewBox="0 0 46 40"><path d="M4 36h38M10 36l6-18M23 36V10M36 36l-6-18" stroke="#9aa39d" stroke-width="3"/></svg></div>
    <div class="product-row"><span class="num">03</span><span class="name">Soil Treatments</span><svg width="46" height="46" viewBox="0 0 46 46"><path d="M4 42h38M23 42V18M23 24c-10 0-14-8-14-14 8 0 14 4 14 14zM23 20c0-8 6-12 14-12 0 8-6 12-14 12z" stroke="#9aa39d" stroke-width="3" fill="none"/></svg></div>
    <div class="product-row"><span class="num">04</span><span class="name">Control Products</span><svg width="46" height="50" viewBox="0 0 46 50"><path d="M23 4l6 18 14-6-10 14 10 4-20 2v12M23 4l-6 18-14-6 10 14-10 4 20 2" stroke="#9aa39d" stroke-width="3" fill="none"/></svg></div>
    <div class="product-row" style="border-bottom:none"><span class="num">05</span><span class="name">Turf Equipment</span><svg width="56" height="46" viewBox="0 0 56 46"><path d="M4 4l8 26h30" stroke="#9aa39d" stroke-width="3" fill="none"/><circle cx="16" cy="38" r="5" fill="none" stroke="#9aa39d" stroke-width="3"/><circle cx="42" cy="38" r="7" fill="none" stroke="#9aa39d" stroke-width="3"/></svg></div>
  </div>
</section>

<section class="grants">
  <h2 class="abs band-title display" style="top:72px">Supporting Local Sports<br>&amp; Community Grounds</h2>
  <div class="card grant-card" style="left:150px">
    <h3 class="display">Who Can Apply<br>Eligibility</h3>
    <ul><li>Local sports clubs and teams (soccer, rugby)</li><li>Schoolinstitutions with sports fields</li><li>Council or community-managed grounds</li></ul>
  </div>
  <div class="card grant-card" style="left:456px">
    <h3 class="display">What the<br>Grants Cover</h3>
    <ul><li>Local sports clubs and teams (soccer, rugby)</li><li>Schoolinstitutions with sports fields</li><li>Council or community-managed grounds</li></ul>
  </div>
  <div class="card grant-card" style="left:762px">
    <h3 class="display">How to<br>Apply</h3>
    <ul><li>Local sports clubs and teams (soccer, rugby)</li><li>Schoolinstitutions with sports fields</li><li>Council or community-managed grounds</li></ul>
  </div>
</section>

<section class="gallery">
  <h2 class="abs dark-title display" style="top:98px">See the Difference We Make</h2>
  <div class="gal gal-left" role="img" aria-label="Soil treatment work shown outdoors">Soil Treatments</div>
  <div class="gal gal-right" role="img" aria-label="Wrapped roll of seed beside a green field">Grass Seeds</div>
  <div class="gal gal-center" role="img" aria-label="Sprinkler watering a floodlit stadium pitch">Turf Fertilizers</div>
  <svg class="abs" style="left:150px;top:600px" width="900" height="80" viewBox="0 0 900 80">
    <path d="M2 10 Q450 110 898 10" fill="none" stroke="#111" stroke-width="2"/>
    <circle cx="175" cy="44" r="6" fill="#fff" stroke="#0c3a1c" stroke-width="3"/>
    <circle cx="727" cy="44" r="6" fill="#fff" stroke="#0c3a1c" stroke-width="3"/>
    <circle cx="450" cy="60" r="18" fill="#0c3a1c"/>
    <circle cx="450" cy="60" r="11" fill="#fff"/>
    <path d="M450 54v12M444 60h12" stroke="#0c3a1c" stroke-width="3"/>
  </svg>
</section>

<section class="contact">
  <h2 class="abs dark-title display" style="top:88px">Get Your Turf Looking Its Best</h2>
  <div class="abs contact-item" style="left:170px">
    <div class="contact-icon"><svg width="22" height="22" viewBox="0 0 24 24"><path d="M5 3l4 1 2 5-3 2a12 12 0 005 5l2-3 5 2 1 4-3 2C10 21 3 14 3 6z" fill="#fff"/></svg></div>
    <p>(410) 555-0148<br>(410) 555-0172</p>
  </div>
  <div class="abs contact-item" style="left:435px">
    <div class="contact-icon"><svg width="20" height="24" viewBox="0 0 20 24"><path d="M10 1a8 8 0 00-8 8c0 6 8 14 8 14s8-8 8-14a8 8 0 00-8-8z" fill="#fff"/><circle cx="10" cy="9" r="3" fill="#0c3a1c"/></svg></div>
    <p>48 Fairway Rd. Northreach,<br>QLD 4740</p>
  </div>
  <div class="abs contact-item" style="left:715px">
    <div class="contact-icon"><svg width="22" height="18" viewBox="0 0 22 18"><rect x="1" y="1" width="20" height="16" fill="#fff"/><path d="M1 2l10 8 10-8" stroke="#0c3a1c" stroke-width="2" fill="none"/></svg></div>
    <p>hello@cobaltfield<br>.com</p>
  </div>
  <div class="field" style="left:214px;top:292px;width:378px">First Name</div>
  <div class="field" style="left:608px;top:292px;width:378px">Last Name</div>
  <div class="field" style="left:214px;top:352px;width:378px">Phone Number</div>
  <div class="field" style="left:608px;top:352px;width:378px">Email</div>
  <div class="field" style="left:214px;top:412px;width:772px;height:110px">Messages</div>
  <div class="abs btn submit">Submit</div>
</section>

<footer class="footer">
  <div class="abs foot-logo">COBALT FIELD<small>SERVICES</small></div>
  <p class="abs foot-tag">Lorem Ipsum Dolor Sit Amet Consectetur. Leo Ornare Purus Id Ut Sem.</p>
  <p class="abs foot-about">Lorem Ipsum Dolor Sit Amet Consectetur. Aliquam Dolor Consequat Eu Ac Mus Orci Amet Erat Molestie Vitae.</p>
  <div class="abs socials"><span></span><span></span><span></span><span></span></div>
  <nav class="abs foot-nav"><span>Home</span><span>About Us</span><span>Services</span><span>Products</span><span>Grants Initiative</span><span>Gallery</span><span>Contact us</span></nav>
  <div class="abs foot-rule"></div>
  <div class="abs foot-legal"><span>Copyright © 2025 All Right Reserved</span><span>Privacy Policy</span><span>Terms Of Service</span><span>Cookies Settings</span></div>
</footer>

</body>
</html>
```